Accounting Practice Business Card Design

I have a logo I am happy for you to use in the design of the Business Card.
You can edit and change colours as you please, I am not fixated on it.
I am looking for a modern and clean overall feel for the finished design.

The business is a small accounting practice who thrives on word of mouth referrals and this card will be given to all current and prospect clients.

Industry/Entity Type

Accountant

Contact Information for Business Card

Marcus Elwin
Level 5, 8 Corvale Ridge Road
ASHGROVE RISE VIC 3187
Phone: 9481 3057
Email: melwin@mrfaccountants.com.au
Web: www.mrfaccountants.com.au

Font styles to use
Serif
Sans Serif

Colors
0555a3
3277b5
85acd3
0393ce
33a6d7
85cae6
00a990
33b8a4
9bcb3c

Requirements
Must have
• "The end to your tax problems begin with us"
• "A referral from you is our greatest compliment"
Nice to have
• Modern clean professional

```html
<!DOCTYPE html>
<html lang="en">
<head>
<meta charset="utf-8">
<title>MRF Accountants – Business Card</title>
<link rel="stylesheet" href="https://fonts.googleapis.com/css2?family=Arimo:wght@400;700&display=swap">
<style>
  :root {
    --blue-deep: #0555a3;
    --blue-mid: #3277b5;
    --green: #4f8a1f;
    --green-light: #9bcb3c;
    --ink: #222428;
    --card: #ffffff;
    --backdrop: #e6e8eb;
  }
  * { box-sizing: border-box; margin: 0; padding: 0; }
  html, body {
    width: 1200px; height: 997px; overflow: hidden;
    background: var(--backdrop);
    font-family: "Arimo", Arial, sans-serif;
  }
  .sheet {
    width: 1200px; height: 997px;
    display: flex; flex-direction: column;
    align-items: center; justify-content: center; gap: 52px;
  }
  .card {
    position: relative;
    width: 760px; height: 424px;
    background: var(--card);
    border-radius: 22px;
    overflow: hidden;
    box-shadow: 0 6px 22px rgba(0,0,0,.14);
  }
  .brand-name {
    color: var(--blue-deep);
    font-weight: 700;
    letter-spacing: 2px;
    line-height: 1;
    white-space: nowrap;
  }

  /* Front */
  .card--front .brand-name {
    position: absolute; left: 0; right: 0; top: 118px;
    text-align: center; font-size: 58px;
  }
  .card--front .tagline {
    position: absolute; left: 0; right: 0; top: 238px;
    text-align: center;
    color: var(--blue-mid);
    font-size: 19px; letter-spacing: 1.5px;
  }
  .card--front .band {
    position: absolute; left: 0; right: 0; bottom: 14px; height: 54px;
    background: var(--blue-deep);
    color: #fff;
    display: flex; align-items: center; justify-content: center;
    font-size: 19px; letter-spacing: 1.5px;
  }
  .card--front .strip {
    position: absolute; left: 0; right: 0; bottom: 0; height: 14px;
    background: var(--green);
  }

  /* Back */
  .card--back .brand-name {
    position: absolute; left: 52px; top: 62px; font-size: 40px;
  }
  .person {
    position: absolute; right: 48px; top: 58px; text-align: right;
  }
  .person__name {
    color: var(--blue-deep); font-weight: 700; font-size: 24px; letter-spacing: .5px;
  }
  .person__role {
    color: var(--green); font-size: 16px; margin-top: 3px;
  }
  .contact {
    position: absolute; right: 48px; top: 150px;
    list-style: none; text-align: right;
    color: var(--ink); font-size: 17px;
  }
  .contact li {
    display: flex; align-items: center; justify-content: flex-end;
    gap: 10px; height: 30px;
  }
  .contact svg { width: 22px; height: 22px; flex: none; }
  .address {
    position: absolute; left: 52px; bottom: 84px;
    color: var(--green); font-size: 18px; line-height: 1.35;
    font-style: normal;
  }
  .card--back .rule {
    position: absolute; left: 0; right: 0; bottom: 60px; height: 5px;
    background: var(--blue-deep);
  }
  .card--back .band {
    position: absolute; left: 0; right: 0; bottom: 0; height: 60px;
    background: var(--green);
    color: #fff;
    display: flex; align-items: center; justify-content: center;
    font-size: 19px; letter-spacing: 1.2px;
  }
</style>
</head>
<body>
<main class="sheet">

  <section class="card card--front" aria-label="Card front">
    <div class="brand-name">MRF ACCOUNTANTS</div>
    <p class="tagline">THE END TO YOUR TAX PROBLEMS BEGIN WITH US</p>
    <div class="band">A REFERRAL FROM YOU IS OUR GREATEST COMPLIMENT</div>
    <div class="strip"></div>
  </section>

  <section class="card card--back" aria-label="Card back">
    <div class="brand-name">MRF ACCOUNTANTS</div>

    <div class="person">
      <div class="person__name">MARCUS ELWIN</div>
      <div class="person__role">Managing Director</div>
    </div>

    <ul class="contact">
      <li>9481 3057
        <svg viewBox="0 0 22 22" aria-hidden="true"><circle cx="11" cy="11" r="11" fill="var(--green)"/><path d="M7 6.5c.6-.6 1.4-.5 1.8.1l1 1.5c.3.5.2 1-.2 1.4l-.6.5c.5 1.2 1.5 2.2 2.7 2.7l.5-.6c.4-.4.9-.5 1.4-.2l1.5 1c.6.4.7 1.2.1 1.8l-.7.7c-3.1.6-7.8-4.1-7.2-7.2z" fill="#fff"/></svg>
      </li>
      <li>melwin@mrfaccountants.com.au
        <svg viewBox="0 0 22 22" aria-hidden="true"><circle cx="11" cy="11" r="11" fill="var(--green)"/><rect x="5.5" y="7" width="11" height="8" rx="1" fill="#fff"/><path d="M5.8 7.4 11 11.5l5.2-4.1" stroke="var(--green)" stroke-width="1.2" fill="none"/></svg>
      </li>
      <li>www.mrfaccountants.com.au
        <svg viewBox="0 0 22 22" aria-hidden="true"><circle cx="11" cy="11" r="11" fill="var(--green)"/><circle cx="11" cy="11" r="5.5" stroke="#fff" stroke-width="1.3" fill="none"/><ellipse cx="11" cy="11" rx="2.3" ry="5.5" stroke="#fff" stroke-width="1.1" fill="none"/><path d="M5.5 11h11" stroke="#fff" stroke-width="1.1"/></svg>
      </li>
    </ul>

    <address class="address">
      Level 5, 8 Corvale Ridge Road<br>
      Ashgrove Rise Vic 3187
    </address>

    <div class="rule"></div>
    <div class="band">CALL US OR VISIT US FOR AN OBLIGATION FREE CONSULTATION.</div>
  </section>

</main>
</body>
</html>
```